Website Graphics

We need 1 page of website graphics for a company called 'RingVantage.' We are a cloud-based dialing solution for sales agents making outbound calling campaigns. Our software application sits on top of Dealbrook.com and accelerates the entire sales process through automation and multi-line dialing. Our website has a 'Features' page (http://ringvantage.example/features/) in need of 13 graphics to replace current placeholders.

We would like to see simple designs that blend well with the look and feel of our current website theme, specifically the colors blue, white, and silver. The designs should feel sleek, 3-D, clean, minimalistic, and modern.

For the Feature 'Native Design' (http://ringvantage.example/features/#tab-id-1) we would like a graphic that shows that our software is extremely secure and reliable.

For the Features 'Preview Mode'(http://ringvantage.example/features/#tab-id-2), 'Preview Auto' (http://ringvantage.example/features/#tab-id-3), and 'RingVantage Mode' (http://ringvantage.example/features/#tab-id-4), we would like 3-D backdrops of Zentrons and Plivas with a screenshot layered on top. I will upload two screen shots. The first can be used for both 'Preview Mode' and 'Preview Auto,' the second is for 'RingVantage Mode.'

For 'Post-Call Automation' (http://ringvantage.example/features/#tab-id-5) we are looking for a design that highlights efficiency, speed, and powerful software automation.

For 'Regional ID' (http://ringvantage.example/features/#tab-id-6) we are looking for a graphic that incorporates a map of North America.

For "Instant Priority Queue' (http://ringvantage.example/features/#tab-id-9) we are looking for a graphic that shows speed and instant reaction the second a notification comes through.

For 'Live Dashboards' (http://ringvantage.example/features/#tab-id-10) we are looking for a graphic very similar to the one currently up on the site under that feature. It is a great example of a design that is visually appealing and 3-D.

For the rest of the features, we are open to design interpretations that reflect the description of each feature and help website visitor's visually understand what that feature does.

For reference, here is a website design with graphics that inspire us: http://www.kelvra.example/company/what-is-kelvra
Updates

Updated brief with detailed descriptions of our vision for each graphic.

Target Market(s)

Professional demographic; companies using Dealbrook.com with sales teams that outbound dial to customers and potential leads.

Industry/Entity Type

Software

Requirements
Must have
• The webpage http://ringvantage.example/features/ must have 13 images to fill the white space under each feature description.

```html
<!DOCTYPE html>
<html lang="en">
<head>
<meta charset="utf-8">
<title>Features – Prismline Dialer</title>
<link href="https://fonts.googleapis.com/css2?family=Montserrat:wght@500&family=Open+Sans:wght@400;600;700&display=swap" rel="stylesheet">
<style>
  :root {
    --brand-blue: #52b0d6;
    --nav-text: #555555;
    --nav-active: #333333;
    --body-text: #444444;
    --tab-text: #666666;
    --tab-icon: #777777;
    --border: #e2e2e2;
    --footer-band: #dcdadc;
    --social: #7b7b7b;
    --white: #ffffff;
    --art-teal: #c9e9ee;
    --art-warm: #f6e3d6;
  }
  * { box-sizing: border-box; margin: 0; padding: 0; }
  html, body { width: 1200px; height: 1104px; overflow: hidden; background: var(--white); }
  body { font-family: "Open Sans", Arial, sans-serif; color: var(--body-text); position: relative; }

  .site-header {
    position: absolute; top: 0; left: 0; width: 1200px; height: 110px;
    border-top: 1px solid #eeeeee; margin-top: 24px;
  }
  .brand {
    position: absolute; left: 114px; top: 8px; text-decoration: none;
    display: flex; flex-direction: column; align-items: flex-start; gap: 6px;
  }
  .brand-square { width: 62px; height: 62px; background: var(--brand-blue); margin-left: 6px; }
  .brand-name { font-size: 10px; font-weight: 400; color: var(--brand-blue); letter-spacing: .2px; }

  .main-nav {
    position: absolute; right: 120px; top: 40px;
    display: flex; gap: 24px; list-style: none;
  }
  .main-nav a {
    font-size: 12.5px; font-weight: 600; color: var(--nav-text);
    text-decoration: none; text-transform: uppercase;
  }
  .main-nav .is-current a { color: var(--nav-active); }

  .page-title {
    position: absolute; top: 150px; left: 0; width: 1200px; text-align: center;
    font-family: "Montserrat", Arial, sans-serif; font-weight: 500;
    font-size: 76px; letter-spacing: 2px; color: var(--brand-blue); line-height: 1;
  }
  .page-lead {
    position: absolute; top: 238px; left: 0; width: 1200px; text-align: center;
    font-size: 19.5px; font-weight: 400; color: var(--brand-blue);
  }

  .feature-tabs {
    position: absolute; left: 115px; top: 300px; width: 965px; height: 579px;
    border: 1px solid var(--border);
  }
  .tab-list { position: absolute; left: 0; top: 0; width: 234px; list-style: none; }
  .tab-list li {
    height: 44.5px; display: flex; align-items: center; gap: 8px;
    padding-left: 15px; border-bottom: 1px solid var(--border);
    border-right: 1px solid var(--border);
    font-size: 11px; color: var(--tab-text); text-transform: uppercase;
  }
  .tab-list li:last-child { border-bottom: none; }
  .tab-list li.is-active { border-right-color: transparent; font-weight: 600; color: #333; }
  .tab-list svg { width: 12px; height: 12px; fill: var(--tab-icon); flex: none; }
  .tab-list li.is-active svg { fill: #333; }

  .tab-panel { position: absolute; left: 234px; top: 0; right: 0; bottom: 0; }
  .tab-copy {
    margin: 20px 18px 0; padding-bottom: 12px; border-bottom: 1px solid var(--border);
    font-size: 12.5px; line-height: 20.5px; text-align: center; color: var(--body-text);
  }
  .feature-art {
    position: absolute; left: 201px; top: 152px; width: 261px; height: 379px;
    background: linear-gradient(180deg, var(--art-teal) 0%, var(--art-warm) 100%);
  }

  .site-footer {
    position: absolute; left: 0; top: 925px; width: 1200px; height: 134px;
    background: var(--footer-band);
  }
  .social { position: absolute; left: 116px; top: 42px; display: flex; gap: 6px; list-style: none; }
  .social li { width: 30px; height: 30px; border-radius: 50%; background: var(--social); }
  .copyright {
    position: absolute; left: 115px; top: 1077px; font-size: 11px; color: #222;
  }
  .copyright .sep { color: var(--brand-blue); padding: 0 4px; }
</style>
</head>
<body>
  <header class="site-header">
    <a class="brand" href="#" aria-label="Prismline Dialer home">
      <span class="brand-square"></span>
      <span class="brand-name">Prismline Dialer</span>
    </a>
    <ul class="main-nav">
      <li class="is-current"><a href="#">Features</a></li>
      <li><a href="#">Native vs. Integrated</a></li>
      <li><a href="#">Customers</a></li>
      <li><a href="#">Company</a></li>
      <li><a href="#">Blog</a></li>
      <li><a href="#">Request Demo</a></li>
    </ul>
  </header>

  <h1 class="page-title">FEATURES</h1>
  <p class="page-lead">Close deals fast with the power of cloud automation and multi-line dialing at your fingertips.</p>

  <section class="feature-tabs">
    <ul class="tab-list">
      <li><svg viewBox="0 0 12 12"><rect x="2" y="5" width="8" height="7"/><path d="M3.5 5V3.5a2.5 2.5 0 0 1 5 0V5h-1.2V3.5a1.3 1.3 0 0 0-2.6 0V5z"/></svg>Native Design</li>
      <li><svg viewBox="0 0 12 12"><circle cx="5" cy="5" r="3.5" fill="none" stroke="#777" stroke-width="1.5"/><path d="M7.5 7.5l3.5 3.5" stroke="#777" stroke-width="1.8"/></svg>Preview Mode</li>
      <li><svg viewBox="0 0 12 12"><path d="M7 1l5 4.5L7 10V7.5C3.5 7.5 1.5 9 0 11c.5-4 2.5-6.5 7-7z"/></svg>Preview Auto</li>
      <li><svg viewBox="0 0 12 12"><path d="M9.5 1l2 2-1 2.5L9 5 5 9l.5 1.5L3 11.5l-2-2C1 5 5 1 9.5 1z"/></svg>RingVantage Mode</li>
      <li><svg viewBox="0 0 12 12"><rect x="2.5" y="4" width="7" height="6" rx="1"/><path d="M2.5 3.5a3.5 3 0 0 1 7 0z"/><rect x="0.5" y="4.5" width="1.3" height="4" rx=".6"/><rect x="10.2" y="4.5" width="1.3" height="4" rx=".6"/></svg>Post-Call Automation</li>
      <li class="is-active"><svg viewBox="0 0 12 12"><path d="M6 1l6 5h-1.8v5H7.5V8h-3v3H1.8V6H0z"/></svg>Regional ID</li>
      <li><svg viewBox="0 0 12 12"><rect x="4" y="0.5" width="4" height="7" rx="2"/><path d="M2.5 5.5a3.5 3.5 0 0 0 7 0" fill="none" stroke="#777"/><rect x="5.5" y="9" width="1" height="2"/><rect x="4" y="11" width="4" height="1"/></svg>Whisper Mode</li>
      <li><svg viewBox="0 0 12 12"><circle cx="4" cy="3.5" r="2.3"/><path d="M0 11c0-3 1.8-4.5 4-4.5S8 8 8 11z"/><circle cx="8.5" cy="3.5" r="2"/><path d="M9 6.5c2 0 3 1.5 3 4.5H9z"/></svg>Live-Call Monitoring</li>
      <li><svg viewBox="0 0 12 12"><path d="M6 0.5L11.8 11H0.2z"/><rect x="5.4" y="4" width="1.2" height="4" fill="#fff"/><rect x="5.4" y="8.8" width="1.2" height="1.2" fill="#fff"/></svg>Instant Priority Queue</li>
      <li><svg viewBox="0 0 12 12"><rect x="1" y="8" width="2.5" height="3.5"/><rect x="4.7" y="5" width="2.5" height="6.5"/><rect x="8.4" y="1.5" width="2.5" height="10"/></svg>Live Dashboards</li>
      <li><svg viewBox="0 0 12 12"><path d="M9 0.5l2.5 2.5-7 7L1 11l1-3.5z"/></svg>Auto Call Recording</li>
      <li><svg viewBox="0 0 12 12"><circle cx="6" cy="6" r="5.5"/><path d="M3 3c1.5 0 2 1 3 1s1 1.5 0 2-2 .5-2 2" fill="none" stroke="#fff" stroke-width="1"/></svg>Global Recycle</li>
      <li><svg viewBox="0 0 12 12"><path d="M4 2l7-1.5v8a1.8 1.5 0 1 1-1.2-1.4V3L5.2 4v6a1.8 1.5 0 1 1-1.2-1.4z"/></svg>Music</li>
    </ul>

    <div class="tab-panel">
      <p class="tab-copy">No matter where a lead or contact is located, all outbound calls display a regional (local) area code and phone number. Returned calls are automatically re-routed to your desired telephone number. Dramatically increase contact rates by over 50% while penetrating far-reaching markets.</p>
      <div class="feature-art" role="img" aria-label="Illustration: a network of contacts linked by dotted lines above a tablet, with a hand tapping a contact on the screen"></div>
    </div>
  </section>

  <footer class="site-footer">
    <ul class="social" aria-label="Social links">
      <li aria-label="Professional network"></li>
      <li aria-label="Microblog"></li>
      <li aria-label="Video channel"></li>
    </ul>
  </footer>
  <p class="copyright">Copyright © 2014 All Rights Reserved<span class="sep">|</span>Prismline Dialer -</p>
</body>
</html>
```